ZESTORAMA Business Card Design

ZESTORAMA
Zestorama is a food van, serving high vibe delicious food to go. This business is dedicated to healthy delicious feel good food, beauty in service and a sustainable planet.

The van will operate in the south west of western Australia at music festivals events markets wherever people need great food to go!

I like the idea of vibrant green mixed with a yellow?? background with some rays like the sun through the background.
The font needs to say vibrant energetic
TO ME -vibrant energetic font has to appear to be on the move - perhaps with shading??

I like fusha if that works for font? but the colour has to say food too.

I would like a symbol on the card a simple V turned into a womans raised arms. This should be vibrant too.
Thank you
Blessings
Marisol

Target Market(s)

target lovers of healthy high vibe food. music festival goers. age 18- 50 feel. audiance conscious eaters of feel great food

Industry/Entity Type

Events

Contact Information for Business Card

ZESTORAMA
High Vibe Food
Van
Marisol -owner/opperator
0417385960
Face book symbol - ZESTORAMA

on the I would like a logo of a simple V turned into a womans arms up toward the sky flip side

My number and name again
Zestorama- feel great mobile food
Festivals, events, markets & where high vibe food 2 go is appreciated

Requirements
Nice to have
• Moving energetic font
colour that says high vibe and healthy food

a logo that is a simple V turned into a woman's raised arms in gratitude

```html
<!DOCTYPE html>
<html lang="en">
<head>
<meta charset="utf-8">
<title>Zestorama Business Card</title>
<link href="https://fonts.googleapis.com/css2?family=Anton&family=Poppins:wght@600;700&family=Varela+Round&display=swap" rel="stylesheet">
<style>
  :root {
    --stage: #cbcbcb;
    --fuchsia: #ee2a7b;
    --ink: #1a1a1a;
    --white: #ffffff;
    --lime: #8cc63f;
    --citrus: #e3ea2a;
    --leaf: #6fbf3a;
  }
  * { box-sizing: border-box; margin: 0; padding: 0; }
  html, body { width: 1200px; height: 1000px; overflow: hidden; }
  body { background: var(--stage); position: relative; font-family: "Poppins", sans-serif; }

  .card {
    position: absolute; top: 135px; width: 455px; height: 736px;
    box-shadow: 0 6px 14px rgba(0,0,0,.28);
    overflow: hidden; text-align: center; color: var(--fuchsia);
  }
  .card--front { left: 116px; }
  .card--back { left: 637px; }

  .card__burst {
    position: absolute; inset: 0;
    background:
      radial-gradient(circle at 50% 45%, var(--citrus) 0%, rgba(227,234,42,.6) 30%, rgba(140,198,63,0) 70%),
      linear-gradient(160deg, var(--lime), var(--leaf) 50%, var(--lime));
  }

  .brand-mark {
    position: absolute; left: 50%; width: 144px; height: 144px; margin-left: -72px;
    border-radius: 50%; background: var(--fuchsia);
    display: flex; align-items: center; justify-content: center;
    font-family: "Poppins", sans-serif; font-weight: 700; font-size: 22px; color: var(--white);
  }

  .brand-name {
    position: absolute; left: 0; right: 0;
    font-family: "Anton", sans-serif; font-size: 64px; line-height: 1; letter-spacing: 1px;
    color: var(--fuchsia);
  }

  .tagline {
    position: absolute; left: 0; right: 0;
    font-weight: 700; font-size: 25px; line-height: 1.1; color: var(--white);
    text-shadow: -1.5px -1.5px 0 var(--fuchsia), 1.5px -1.5px 0 var(--fuchsia), -1.5px 1.5px 0 var(--fuchsia), 1.5px 1.5px 0 var(--fuchsia);
  }

  .rounded-dark {
    font-family: "Varela Round", sans-serif; font-weight: 400; color: var(--fuchsia);
    text-shadow: -1.5px -1.5px 0 var(--ink), 1.5px -1.5px 0 var(--ink), -1.5px 1.5px 0 var(--ink), 1.5px 1.5px 0 var(--ink);
  }

  .contact-name, .contact-phone {
    position: absolute; left: 0; right: 0; font-weight: 600; font-size: 30px;
  }
  .contact-name { top: 384px; }
  .contact-phone { top: 467px; }

  .social {
    position: absolute; left: 0; right: 0; top: 603px;
    display: flex; justify-content: center; align-items: center; gap: 10px;
    font-weight: 600; font-size: 22px; color: var(--fuchsia);
  }
  .social__square { width: 22px; height: 22px; background: var(--fuchsia); border-radius: 3px; }

  .contact-email { position: absolute; left: 0; right: 0; top: 650px; font-size: 28px; }

  .events { position: absolute; left: 0; right: 0; top: 148px; font-size: 24px; line-height: 1.3; }

  .about {
    position: absolute; left: 30px; right: 30px; top: 392px;
    font-weight: 600; font-size: 23px; line-height: 1.42;
  }
  .about__cta { font-family: "Varela Round", sans-serif; font-size: 24px; }
</style>
</head>
<body>

  <section class="card card--front">
    <div class="card__burst" role="img" aria-label="Sunburst rays in lime green and yellow"></div>
    <div class="brand-mark" style="top:53px;">Zestorama</div>
    <h1 class="brand-name" style="top:208px;">ZESTORAMA</h1>
    <p class="tagline" style="top:285px;">High Vibe Food Van</p>
    <p class="contact-name">Marisol</p>
    <p class="contact-phone">0417385960</p>
    <div class="social"><span class="social__square"></span><span>Chatterbook</span></div>
    <p class="contact-email rounded-dark">hello@zestorama-van.com</p>
  </section>

  <section class="card card--back">
    <div class="card__burst" role="img" aria-label="Sunburst rays in lime green and yellow"></div>
    <h2 class="brand-name" style="top:50px;">ZESTORAMA</h2>
    <p class="tagline" style="top:120px;">Feel Great Food</p>
    <p class="events rounded-dark">@ festivals,<br>community events &amp;<br>private gatherings</p>
    <div class="brand-mark" style="top:248px;">Zestorama</div>
    <p class="about">
      Dedicated to joyous,<br>conscious eating!<br>VIBRANT breakfasts,<br>coconuts &amp; DELICIOUS<br>nourishing soups.<br>Zestorama includes<br>vegetarian, vegan and<br>dairy &amp; gluten free options.<br>
      <span class="about__cta rounded-dark">Got The Vibe?</span>
    </p>
  </section>

</body>
</html>
```